BPH Business Card 2018

Brellmore Chiropractic. We have two locations that we want to advertise on the same card. Calderwick OrthoAxis campus address: 3815 Pemberly Dr., Suite 240, Flowood, MS 39587. Madison address: 426 Larkmoor Dr., Building D., Madison, MS 39674. website: www.drbrellmore.example. o:(601)555-0148 f:(601)555-0173

Target Market(s)

Health care decision makers: primary care doctors and mothers

Contact Information for Business Card

I have no idea; up for any suggestions and I'd do much better picking from examples versus describing what I'm looking for. We are in a very high end location and would like the cards to look really sharp.

Requirements
Must have
• My name, Tobias R Venmark, D.C.

```html
<!DOCTYPE html>
<html lang="en">
<head>
<meta charset="utf-8">
<title>Brellmore Chiropractic – Business Card</title>
<link rel="stylesheet" href="https://fonts.googleapis.com/css2?family=Roboto:wght@300;400;500;700&display=swap">
<style>
  :root {
    --backdrop: #2a2a2c;
    --card-light: #fbfbfb;
    --card-dark: #161616;
    --ink-dark: #111111;
    --ink-muted: #555555;
    --ink-light: #f4f4f4;
    --rule-light: #cfcfcf;
  }
  * { box-sizing: border-box; margin: 0; padding: 0; }
  html, body {
    width: 1200px; height: 900px; overflow: hidden;
    background: var(--backdrop);
    font-family: "Roboto", Arial, sans-serif;
  }
  .stage {
    width: 1200px; height: 900px;
    display: flex; flex-direction: column;
    align-items: center; justify-content: center; gap: 34px;
  }
  .card {
    width: 700px; height: 400px; position: relative;
    border-radius: 2px;
  }
  /* Front */
  .card-front { background: var(--card-light); }
  .brand-mark {
    position: absolute; left: 150px; top: 110px;
    display: flex; align-items: center; gap: 22px;
  }
  .brand-square {
    width: 84px; height: 84px; background: var(--ink-dark);
  }
  .brand-name {
    color: var(--ink-dark); font-weight: 400;
    text-transform: uppercase; line-height: 1.05;
  }
  .brand-name .line-main { display: block; font-size: 42px; letter-spacing: 1px; }
  .brand-name .line-sub { display: block; font-size: 26px; letter-spacing: 3px; }
  .front-site {
    position: absolute; left: 0; right: 0; top: 262px;
    text-align: center; font-size: 17px; font-weight: 300;
    letter-spacing: 6px; color: var(--ink-muted); text-transform: uppercase;
  }
  /* Back */
  .card-back { background: var(--card-dark); color: var(--ink-light); }
  .practitioner {
    position: absolute; right: 370px; top: 148px;
    font-size: 25px; font-weight: 700; letter-spacing: 0.5px;
    text-transform: uppercase; white-space: nowrap;
  }
  .divider {
    position: absolute; left: 352px; top: 118px;
    width: 1px; height: 116px; background: var(--rule-light);
  }
  .contact-list {
    position: absolute; left: 374px; top: 126px;
    list-style: none; font-size: 18px; font-weight: 400;
  }
  .contact-list li {
    display: flex; align-items: center; gap: 12px; height: 32px;
  }
  .contact-list svg { width: 17px; height: 17px; fill: var(--ink-light); flex: none; }
  .addresses {
    position: absolute; left: 0; right: 0; top: 270px;
    text-align: center; font-size: 17px; font-weight: 400; line-height: 1.65;
  }
</style>
</head>
<body>
<main class="stage">
  <section class="card card-front" aria-label="Card front">
    <div class="brand-mark">
      <span class="brand-square" aria-hidden="true"></span>
      <span class="brand-name">
        <span class="line-main">Brellmore</span>
        <span class="line-sub">Chiropractic</span>
      </span>
    </div>
    <p class="front-site">www.drbrellmore.example</p>
  </section>

  <section class="card card-back" aria-label="Card back">
    <h1 class="practitioner">Tobias R Venmark, D.C.</h1>
    <span class="divider" aria-hidden="true"></span>
    <ul class="contact-list">
      <li>
        <svg viewBox="0 0 24 24" aria-hidden="true"><path d="M6.6 10.8a15.1 15.1 0 0 0 6.6 6.6l2.2-2.2c.3-.3.7-.4 1-.2 1.1.4 2.3.6 3.6.6.6 0 1 .4 1 1V20c0 .6-.4 1-1 1A17 17 0 0 1 3 4c0-.6.4-1 1-1h3.5c.6 0 1 .4 1 1 0 1.3.2 2.5.6 3.6.1.3 0 .7-.2 1z"/></svg>
        <span>(601)555-0148</span>
      </li>
      <li>
        <svg viewBox="0 0 24 24" aria-hidden="true"><path d="M7 3h10v5H7z"/><path d="M4 9h16a2 2 0 0 1 2 2v6h-4v4H6v-4H2v-6a2 2 0 0 1 2-2zm4 7v3h8v-3z"/></svg>
        <span>(601)555-0173</span>
      </li>
      <li>
        <svg viewBox="0 0 24 24" aria-hidden="true"><path d="M12 2a10 10 0 1 0 0 20 10 10 0 0 0 0-20zm6.9 9h-3a15 15 0 0 0-1.3-5.6A8 8 0 0 1 18.9 11zM12 4.1c.9 1.2 1.8 3.5 1.9 6.9h-3.8c.1-3.4 1-5.7 1.9-6.9zM9.4 5.4A15 15 0 0 0 8.1 11h-3a8 8 0 0 1 4.3-5.6zM5.1 13h3a15 15 0 0 0 1.3 5.6A8 8 0 0 1 5.1 13zm6.9 6.9c-.9-1.2-1.8-3.5-1.9-6.9h3.8c-.1 3.4-1 5.7-1.9 6.9zm2.6-1.3a15 15 0 0 0 1.3-5.6h3a8 8 0 0 1-4.3 5.6z"/></svg>
        <span>www.drbrellmore.example</span>
      </li>
    </ul>
    <address class="addresses">
      Calderwick OrthoAxis campus : 3815 Pemberly Dr., Suite 240, Flowood, MS 39587.<br>
      Madison address: 426 Larkmoor Dr., Building D., Madison, MS 39674.
    </address>
  </section>
</main>
</body>
</html>
```